Want to market to schools to offer free chair massages for teacher and staff of the schools

This postcard will be mailed to all public schools in the U.S.

We want the schools to call our company to have a massage therapist provide free chair massages to the teachers and staff at their next School Improvement or Teacher Institute day.

want to make the postcard fun and inviting.

The postcard is 4 1/4" X 6"

FRONT AND BACK DESIGN.

For the back of postcard design, I have attached a template. You can use all the space except where the return label and stamp will go.

Target Market(s)

Target is schools and teachers

Industry/Entity Type

Teacher

```html
<!DOCTYPE html>
<html lang="en">
<head>
<meta charset="UTF-8">
<title>VitalPath Wellness Centers – Free Chair Massage Postcard</title>
<link rel="stylesheet" href="https://fonts.googleapis.com/css2?family=Arimo:wght@400&family=Fredoka:wght@600&family=Roboto+Condensed:wght@700&display=swap">
<style>
  :root {
    --frame-red: #e8232a;
    --frame-blue: #9fd3f0;
    --frame-green: #9ed08a;
    --paper: #ffffff;
    --paper-tint: #f6f7f9;
    --brand-blue: #1a4fa0;
    --brand-text: #3a3a3a;
    --headline-purple: #c51ee6;
    --body-blue: #1560d8;
    --cta-blue: #1a74e0;
    --burst-red: #e8101a;
    --burst-text: #ffffff;
    --photo-light: #f3e6dc;
    --photo-mid: #e2c4ac;
  }
  html, body {
    margin: 0;
    padding: 0;
    overflow: hidden;
    background: var(--paper);
  }
  .postcard {
    position: relative;
    width: 1200px;
    height: 850px;
    overflow: hidden;
    background: var(--paper);
  }
  .postcard__frames {
    position: absolute;
    inset: 0;
  }
  .brand {
    position: absolute;
    left: 60px;
    top: 60px;
    display: flex;
    align-items: center;
    gap: 18px;
  }
  .brand__dot {
    width: 120px;
    height: 120px;
    border-radius: 50%;
    background: var(--brand-blue);
    flex: none;
  }
  .brand__name {
    font-family: "Arimo", Arial, sans-serif;
    font-weight: 400;
    color: var(--brand-text);
    line-height: 1;
  }
  .brand__name-main {
    display: block;
    font-size: 54px;
    letter-spacing: -1px;
  }
  .brand__name-sub {
    display: block;
    font-size: 33px;
    margin-top: 6px;
  }
  .headline {
    position: absolute;
    left: 538px;
    top: 72px;
    width: 600px;
    margin: 0;
    text-align: center;
    font-family: "Fredoka", "Comic Sans MS", sans-serif;
    font-weight: 600;
    font-size: 34px;
    line-height: 44px;
    color: var(--headline-purple);
  }
  .body-copy {
    position: absolute;
    left: 56px;
    top: 262px;
    width: 1070px;
    font-family: "Arimo", Arial, sans-serif;
    font-size: 31px;
    line-height: 42px;
    color: var(--body-blue);
  }
  .body-copy p {
    margin: 0 0 42px;
  }
  .offer-band {
    position: absolute;
    left: 46px;
    top: 617px;
    width: 1108px;
    height: 188px;
    background: var(--paper);
  }
  .offer-band__photo {
    position: absolute;
    top: 0;
    height: 188px;
  }
  .offer-band__photo--left {
    left: 0;
    width: 314px;
    background: linear-gradient(90deg, var(--photo-mid), var(--photo-light) 70%, var(--paper));
  }
  .offer-band__photo--right {
    right: 0;
    width: 300px;
    background: linear-gradient(270deg, var(--photo-mid), var(--photo-light) 70%, var(--paper));
  }
  .cta {
    position: absolute;
    font-family: "Roboto Condensed", "Arial Narrow", sans-serif;
    font-weight: 700;
    color: var(--cta-blue);
    text-transform: uppercase;
    font-size: 27px;
    line-height: 1;
    white-space: nowrap;
  }
  .cta--line1 { left: 303px; top: 28px; }
  .cta--line2 { left: 374px; top: 57px; }
  .cta__phone {
    position: absolute;
    left: 332px;
    top: 93px;
    font-family: "Roboto Condensed", "Arial Narrow", sans-serif;
    font-weight: 700;
    font-size: 56px;
    letter-spacing: -1.5px;
    line-height: 1;
    color: var(--cta-blue);
    white-space: nowrap;
  }
  .free-burst {
    position: absolute;
    left: 680px;
    top: 28px;
    width: 148px;
    height: 148px;
  }
</style>
</head>
<body>
<div class="postcard">
  <svg class="postcard__frames" width="1200" height="850" viewBox="0 0 1200 850" aria-hidden="true">
    <rect x="0.5" y="0.5" width="1199" height="849" fill="var(--paper-tint)" stroke="var(--frame-red)" stroke-width="1"/>
    <rect x="23" y="20" width="1154" height="809" fill="var(--paper)" stroke="var(--frame-blue)" stroke-width="1.5"/>
    <rect x="46" y="44" width="1108" height="761" fill="var(--paper-tint)" stroke="var(--frame-green)" stroke-width="1"/>
  </svg>

  <div class="brand">
    <div class="brand__dot"></div>
    <div class="brand__name">
      <span class="brand__name-main">VitalPath</span>
      <span class="brand__name-sub">Wellness Centers</span>
    </div>
  </div>

  <h1 class="headline">Free Chair Massage<br>at your next School Improvement<br>&amp; Teacher Institute Day…!!</h1>

  <div class="body-copy">
    <p>Call to arrange complimentary chair massages with VitalPath Wellness Centers. We will send one of our affiliate therapists to your school and provide chair massages to Teachers and Staff.</p>
    <p>Massage helps relax tight and stiff muscles melting away stress.&nbsp; The therapist aims to release chronic stiffness in the neck and back.</p>
    <p>It’s our way to show appreciation to the teachers.</p>
  </div>

  <div class="offer-band">
    <div class="offer-band__photo offer-band__photo--left" role="img" aria-label="Photo of a relaxed woman lying down receiving a shoulder massage"></div>
    <div class="offer-band__photo offer-band__photo--right" role="img" aria-label="Photo of a relaxed man lying down receiving a back massage"></div>

    <div class="cta cta--line1">Call today to reserve</div>
    <div class="cta cta--line2">a date for your school</div>
    <div class="cta__phone">1-800-555-0142</div>

    <svg class="free-burst" viewBox="-85 -85 170 170" role="img" aria-label="It is Free">
      <g fill="var(--burst-red)">
        <rect x="-58" y="-58" width="116" height="116"/>
        <rect x="-58" y="-58" width="116" height="116" transform="rotate(15)"/>
        <rect x="-58" y="-58" width="116" height="116" transform="rotate(30)"/>
        <rect x="-58" y="-58" width="116" height="116" transform="rotate(45)"/>
        <rect x="-58" y="-58" width="116" height="116" transform="rotate(60)"/>
        <rect x="-58" y="-58" width="116" height="116" transform="rotate(75)"/>
      </g>
      <g transform="rotate(-32)" fill="var(--burst-text)" font-family="Arimo, Arial, sans-serif" text-anchor="middle">
        <text x="-4" y="-20" font-size="22">It is</text>
        <text x="0" y="24" font-size="50">Free</text>
      </g>
    </svg>
  </div>
</div>
</body>
</html>
```